Post Card Notification - rental property registration

We need a post card mailer designed to notify Landlord's of the need to register their rental properties according to local ordinance. Designed for optimal response, the response we are looking for is getting the recipient to go to a URL that will be on the postcard.

The postcards will be sent on behalf on Municipalities (aka communities) that we represent. They notify the Homeowner/Landlord of the need to register their property. We will inform them of the properties we have discovered evidence and registration is required. We are considering a color post card that will include the community logo and the company logo and other formatting graphics that enhance the design to get the result we are looking for.

There will be dynamic content in the design that will be specific tothe community logo, message text, property addresses, URL/Code, etc...

Clarifications 9/10/2018:
I wanted to clarify that this post card is not an advertisement but rather an official notification of the obligation to comply and register the property. We want the design to be professional but not to look like an advertisement.

We are looking for instant credibility. This should come with a focus on the community logo. Whether or not we even show the VELTRASCO logo is optional, I am open to designs without it.

Also, we want to emphasize getting them to the coded link.

None of the designs so far achieve the instant credibility or give enough focus to the getting them to the link.

Lastly, the property list will be an actual list of 1 to 5 properties that are required to be registered by the owner. The design should contemplate an actual list of properties.

If you need a sample community logo you can pull one from veltrasco-example.com or from any U.S. community home page.

One other point of clarification, the postcard will be sent for one community at a time. I see some designs with multiple community logos and that is not accurate. If an owner has rental properties in multiple communities then they will get multiple postcards from us. Each post card will be unique to a specific community.

If the owner has multiple properties in that community then they will be listed (hence the property list of 1 to 5 properties)
Updates

Most of the designs I am reviewing have focused to much on making it look like an advertisement with property images. I wanted to clarify that this should look official. There will be a community logo on the post card. We may not even have the VELTRASCO logo on the card, I am open to designs with or without it. Also, the property list will be a list of properties where evidence has been found that it is rented by the owner. We anticipate this will be 1 to 5 properties in a dynamic list. The design should contemplate this. We want the design to look professional but it does not need to look like an advertisement. It needs to get their attention, and have them instantly recognize it as official (instant credibility) and get them to go to the link. None of the designs so far give enough prominence to the community logo or link that I think will be necessary to achieve this goal.

Target Market(s)

Landlords of rented properties

Industry/Entity Type

Government

Requirements
Must have
• Must look official, from the communities that we are partnered with
Should not have
• This should not look like a Real Estate advertisement

```html
<!DOCTYPE html>
<html lang="en">
<head>
<meta charset="utf-8">
<title>Veltrasco Rental Registration Postcard</title>
<link rel="stylesheet" href="https://fonts.googleapis.com/css2?family=Montserrat:wght@400;500;600;700;800;900&display=swap">
<style>
  :root {
    --bg: #6f6f6f;
    --white: #ffffff;
    --ink: #111111;
    --orange: #f4a51c;
    --orange-soft: #fbb534;
    --navy: #13285e;
    --navy-deep: #0d1d4a;
    --blue: #1f5fae;
    --sky: #3d9be0;
    --grey-text: #444444;
  }
  * { box-sizing: border-box; margin: 0; padding: 0; }
  html, body {
    width: 1200px; height: 1200px; overflow: hidden;
    background: var(--bg);
    font-family: "Montserrat", Arial, sans-serif;
  }
  .canvas { position: relative; width: 1200px; height: 1200px; }
  .postcard {
    position: absolute; left: 180px; width: 840px; height: 520px;
    background: var(--white); overflow: hidden;
    box-shadow: 0 10px 28px rgba(0,0,0,.35);
  }
  .postcard--front { top: 50px; }
  .postcard--back { top: 620px; }

  /* Front */
  .brand {
    position: absolute; left: 120px; top: 36px;
    display: flex; align-items: center; gap: 12px;
  }
  .brand__square { width: 34px; height: 34px; background: var(--orange); }
  .brand__name { font-size: 27px; font-weight: 700; color: var(--ink); letter-spacing: .5px; }
  .warning-band {
    position: absolute; left: 0; top: 108px; width: 500px; height: 70px;
    background: var(--orange);
    display: flex; align-items: center; padding-left: 52px;
  }
  .warning-band__text { font-size: 50px; font-weight: 900; color: var(--ink); letter-spacing: 1px; line-height: 1; }
  .fields { position: absolute; left: 72px; top: 194px; width: 380px; }
  .field {
    display: flex; align-items: flex-end; gap: 4px;
    font-size: 12px; line-height: 15px; font-weight: 700; color: var(--ink); margin-bottom: 7px;
    text-transform: uppercase;
  }
  .field__line { flex: 1; border-bottom: 1.5px dotted #555; height: 10px; }
  .field--stack { line-height: 1.05; }
  .field--stack small { display: block; font-size: 10px; }
  .notice-lead { width: 360px; font-size: 12.5px; color: var(--grey-text); line-height: 1.25; margin-top: 2px; }
  .agency-band {
    position: absolute; left: 0; top: 342px; width: 560px; height: 88px;
    background: var(--navy); color: var(--white);
    padding: 15px 0 0 72px;
  }
  .agency-band__title { font-size: 12.5px; font-weight: 800; text-transform: uppercase; margin-bottom: 11px; }
  .agency-band__row { display: flex; align-items: flex-end; gap: 4px; width: 340px; font-size: 12.5px; font-weight: 700; }
  .agency-band__row .field__line { border-color: #c8d0e6; }
  .agency-band__sub { font-size: 12.5px; margin-top: 3px; }
  .resolve { position: absolute; left: 72px; top: 442px; }
  .resolve__lead { font-size: 12.5px; font-weight: 700; color: var(--ink); margin-bottom: 7px; }
  .resolve__link {
    display: inline-block; background: var(--orange); color: var(--navy);
    font-size: 14px; font-weight: 800; padding: 6px 22px; border-radius: 20px;
  }
  .photo-panel { position: absolute; inset: 0; }

  /* Back */
  .title-band {
    position: absolute; left: 0; top: 0; width: 100%; height: 170px;
    background: var(--orange-soft);
    display: flex; align-items: center; padding: 20px 0 0 70px;
  }
  .title-band__text { font-size: 25px; font-weight: 800; color: var(--ink); text-transform: uppercase; }
  .property-list {
    position: absolute; left: 52px; top: 130px; width: 300px; height: 370px;
    border-radius: 22px; overflow: hidden; background: var(--navy-deep);
    box-shadow: 0 4px 12px rgba(0,0,0,.3);
  }
  .property-list__header {
    background: var(--sky); color: var(--white);
    font-size: 24px; font-weight: 800; text-transform: uppercase;
    padding: 10px 0 8px 32px;
  }
  .property-list__body { padding: 30px 28px 0 32px; color: var(--white); }
  .property-list__field {
    display: flex; align-items: flex-end; gap: 4px;
    font-size: 11.5px; text-transform: uppercase; line-height: 1.3;
  }
  .property-list__field .field__line { border-color: #c8d0e6; height: 8px; }
  .property-list__note { font-size: 12px; line-height: 1.35; margin-top: 26px; }
  .property-list__help { font-size: 12px; line-height: 1.4; margin-top: 22px; text-align: justify; }
  .property-list__help strong { font-weight: 800; }
</style>
</head>
<body>
<main class="canvas">

  <section class="postcard postcard--front">
    <svg class="photo-panel" viewBox="0 0 840 520" role="img" aria-label="Photo of a suburban house with a green lawn under a cloudy sky">
      <defs>
        <linearGradient id="photoTone" x1="0" y1="0" x2="0" y2="1">
          <stop offset="0" stop-color="#5f7d9e"/>
          <stop offset=".45" stop-color="#9fb0c2"/>
          <stop offset=".7" stop-color="#3e5a7d"/>
          <stop offset=".85" stop-color="#4f9a3a"/>
          <stop offset="1" stop-color="#3f8b2b"/>
        </linearGradient>
      </defs>
      <path d="M548 0 C 500 120 480 320 560 520 L 520 520 C 440 330 450 120 508 0 Z" fill="#1f5fae"/>
      <path d="M585 0 C 525 140 515 360 600 520 L 560 520 C 480 330 500 120 548 0 Z" fill="#f4a51c"/>
      <path d="M602 0 L 840 0 L 840 520 L 612 520 C 530 360 540 140 602 0 Z" fill="url(#photoTone)"/>
      <path d="M590 0 C 530 140 520 360 604 520" fill="none" stroke="#ffffff" stroke-width="1.5" stroke-dasharray="4 3"/>
    </svg>

    <div class="brand">
      <span class="brand__square"></span>
      <span class="brand__name">VELTRASCO</span>
    </div>

    <div class="warning-band"><h1 class="warning-band__text">WARNING!!!</h1></div>

    <div class="fields">
      <div class="field">Community Name: <span class="field__line"></span></div>
      <div class="field">Ordinance: <span class="field__line"></span></div>
      <div class="field">Number: <span class="field__line"></span></div>
      <div class="field field--stack"><span>Rental Properties<small>Require Registration:</small></span> <span class="field__line"></span></div>
      <p class="notice-lead">Evidence indicates that one or more properties that you own require registration.</p>
    </div>

    <div class="agency-band">
      <p class="agency-band__title">Veltrasco is working on behalf of</p>
      <div class="agency-band__row">Community Name: <span class="field__line"></span></div>
      <p class="agency-band__sub">to administer their Rental Registration Program.</p>
    </div>

    <div class="resolve">
      <p class="resolve__lead">For more info and to resolve this matter go to:</p>
      <span class="resolve__link">VELTRASCO-EXAMPLE.COM/#CODE#</span>
    </div>
  </section>

  <section class="postcard postcard--back">
    <div class="title-band"><h2 class="title-band__text">Properties Requiring Rental Registration:</h2></div>

    <div class="property-list">
      <h3 class="property-list__header">Property List</h3>
      <div class="property-list__body">
        <div class="property-list__field">Owner Name <span class="field__line"></span></div>
        <div class="property-list__field">Site Address <span class="field__line"></span></div>
        <div class="property-list__field">Property ID <span class="field__line"></span></div>
        <div class="property-list__field">Notification <span class="field__line"></span></div>
        <p class="property-list__note">Go to VELTRASCO-EXAMPLE.COM/<br>#CODE<br>to register, exempt or dispute the rental properties on this list.</p>
        <p class="property-list__help">If you are having problems with the above link you can contact VELTRASCO by calling <strong>(555) 014-2870</strong> or emailing support@veltrasco-example.com</p>
      </div>
    </div>
  </section>

</main>
</body>
</html>
```